Quillcraft Greeting Card Desig

I''m seeking a design for a standard size greeting card that will be blank inside and used to say thank you or other messages to customers. It should be in keeping with our corporate image - see website www.quillcraft-example.com.au The design should incorporate our pen logo and/or abide by colours etc in our style guide.  The look and feel should be clean, fresh, approachable and professional.

Happy for the design to use the pen logo without the words. I will load a version without the text
Size of card - standard greeting card of 11.7cm x 16.6cm (can be either orientation)

Target Market(s)

18+ Years Old

Requirements
Must have
• our logo
• corporate colours

```html
<!DOCTYPE html>
<html lang="en">
<head>
<meta charset="utf-8">
<title>Quillcraft Greeting Card</title>
<link rel="stylesheet" href="https://fonts.googleapis.com/css2?family=Fira+Sans:wght@300;400;700&display=swap">
<style>
  :root {
    --card-green: #a5d300;
    --highlight-lime: #d7f22c;
    --ink: #111111;
    --ink-soft: #2a3300;
    --tagline: #dcf38a;
    --contact-text: #f4fbe0;
    --fold-line: #ffffff;
    --swatch-teal: #00697f;
    --swatch-jade: #3fb58b;
    --swatch-aqua: #50e6f0;
    --swatch-plum: #4a0b46;
    --swatch-orange: #f05a00;
  }
  * { margin: 0; padding: 0; box-sizing: border-box; }
  html, body { width: 1200px; height: 851px; overflow: hidden; background: var(--card-green); }
  body { font-family: "Fira Sans", Arial, sans-serif; }

  .card { position: relative; width: 1200px; height: 851px; background: var(--card-green); overflow: hidden; }

  .fold-line {
    position: absolute; left: 600px; top: 0; height: 851px; width: 0;
    border-left: 2px dashed var(--fold-line); opacity: .8;
  }

  .cover-art { position: absolute; inset: 0; width: 1200px; height: 851px; }

  .brand-mark {
    position: absolute; display: flex; align-items: center; gap: 10px;
    font-weight: 700; color: var(--ink); letter-spacing: -0.5px; white-space: nowrap;
  }
  .brand-mark .brand-square { background: var(--ink); display: block; flex: none; }
  .brand-mark--front { left: 650px; top: 196px; font-size: 36px; line-height: 44px; }
  .brand-mark--front .brand-square { width: 24px; height: 24px; }
  .brand-mark--back { left: 53px; top: 492px; font-size: 22px; line-height: 28px; }
  .brand-mark--back .brand-square { width: 15px; height: 15px; }

  .contact {
    position: absolute; left: 53px; top: 568px;
    color: var(--contact-text); font-size: 12.5px; line-height: 17px; font-weight: 400;
  }
  .contact p + p { margin-top: 17px; }

  .tagline {
    position: absolute; left: 914px; top: 642px;
    color: var(--tagline); font-weight: 300; font-size: 35px; line-height: 44px; white-space: nowrap;
  }

  .swatches { position: absolute; left: 917px; top: 798px; display: flex; height: 53px; }
  .swatch { width: 56.6px; height: 53px; }
  .swatch--teal { background: var(--swatch-teal); }
  .swatch--jade { background: var(--swatch-jade); }
  .swatch--aqua { background: var(--swatch-aqua); }
  .swatch--plum { background: var(--swatch-plum); }
  .swatch--orange { background: var(--swatch-orange); }
</style>
</head>
<body>
<main class="card">
  <svg class="cover-art" viewBox="0 0 1200 851">
    <defs>
      <linearGradient id="penToneFill" x1="0" y1="0" x2="1" y2="0">
        <stop offset="0" stop-color="var(--ink)"/>
        <stop offset="1" stop-color="var(--ink-soft)"/>
      </linearGradient>
    </defs>
    <rect class="highlight-block" x="833" y="40" width="190" height="500" fill="var(--highlight-lime)" transform="rotate(32 928 290)"/>
    <rect class="pen-illustration-area" role="img"
      aria-label="Hand-drawn black brush pen illustration sweeping diagonally across the front"
      x="449" y="355" width="886" height="80" rx="10"
      fill="url(#penToneFill)" transform="rotate(-50 892 395)"/>
  </svg>

  <div class="fold-line"></div>

  <!-- Back panel -->
  <div class="brand-mark brand-mark--back"><span class="brand-square"></span>Quillcraft</div>
  <div class="contact">
    <p>E. info@quillcraft-example.com.au<br>T. 02 9000 1234 or 1300 000 111<br>F. 02 9000 5678</p>
    <p>Head Office Address<br>Suite 12, 48 Harbour Lane<br>Northbank, NSW 2000<br>Australia</p>
    <p>Postal Address<br>PO Box 4021<br>Northbank, NSW 2001</p>
  </div>

  <!-- Front panel -->
  <div class="brand-mark brand-mark--front"><span class="brand-square"></span>Quillcraft</div>
  <h1 class="tagline">Experts in<br>Documentation<br>Resourcing</h1>
  <div class="swatches">
    <span class="swatch swatch--teal"></span>
    <span class="swatch swatch--jade"></span>
    <span class="swatch swatch--aqua"></span>
    <span class="swatch swatch--plum"></span>
    <span class="swatch swatch--orange"></span>
  </div>
</main>
</body>
</html>
```